job report

Designer – Professional Plumbing Job Report Template

Overview

We are seeking a skilled designer to create a professional, easy-to-use Job Report template for a commercial and maintenance plumbing business.
The report will be used for clients, property managers, facilities managers, strata, and retail centres and must clearly communicate findings, works completed, and recommendations in a polished, compliant, and branded format.

The final document must be suitable for PDF delivery, email, and ongoing reuse.

Objectives

Present plumbing works in a clear, professional, and defensible report format

Improve client understanding of findings and recommendations

Provide a repeatable template that can be used across maintenance, reactive, and investigative works

Allow easy insertion of text, tables, and photos

Report Structure (Minimum Inclusions)
1. Cover Page

Company logo and branding

Report title (e.g. Plumbing Job Report / Investigation Report)

Client name

Site address

Job reference / work order number

Date of attendance

Technician / contractor name

2. Client & Site Details

Client / company name

Site address

Contact person

Contact details

Access notes (after-hours, tenant access, etc.)

3. Reason for Attendance

Clear description of why attendance was required

Call-out type (reactive, scheduled maintenance, investigation, emergency, etc.)

Reported issue or scope requested by client

4. Findings / Observations

Detailed findings discovered on site

Condition of pipework, fixtures, drainage, or systems

Any contributing factors identified

Notes on compliance, wear, damage, or risk

(This section should support bullet points and paragraphs.)

5. Works Carried Out

Step-by-step description of works completed

Equipment used (e.g. jetter, CCTV camera, leak detection, flex shaft, etc.)

Repairs, replacements, testing, and verification

Confirmation that systems were tested and operational on completion

6. Photos & Visual Evidence

Clearly labelled photo sections

Before / during / after photos

Space for photo captions and explanations

Logical layout that aligns photos with written findings

7. Recommendations

Clearly separated from works completed

Urgent vs non-urgent recommendations

Preventative maintenance advice

Upgrade or replacement suggestions

Risk-based language where appropriate

8. Limitations & Exclusions

Areas not inspected

Access limitations

Assumptions made during inspection

Items outside scope of works

9. Conclusion

Summary of outcome

Confirmation of current system status

Next steps (if any)

10. Sign-Off

Contractor / technician name

Company name

Date

Optional client acknowledgement section

Design Requirements

Clean, professional layout

Commercial / trade-appropriate styling (not overly creative)

Easy-to-read fonts

Consistent headings and spacing

Logical flow for busy property managers

Editable format (Word / Google Docs / InDesign source file)

Final export-ready PDF version

Bonus (Nice to Have)

Traffic-light system (Green / Amber / Red) for condition reporting

Iconography for findings, repairs, and recommendations

Optional sections for compliance notes (AS/NCC references)

Space for QR codes or job reference numbers

Deliverables

Editable master report template

PDF version

Instructions or notes for ongoing use

```html
<!DOCTYPE html>
<html lang="en">
<head>
<meta charset="utf-8">
<title>Plumbing Job Report – Cover</title>
<link rel="stylesheet" href="https://fonts.googleapis.com/css2?family=Poppins:wght@500;600;800&display=swap">
<style>
  :root {
    --cyan: #55f6ee;
    --orange: #f6bb25;
    --ink: #111111;
    --paper: #eef0f2;
    --paper-soft: #f7f8f9;
    --shadow: rgba(0, 0, 0, 0.35);
  }
  * { margin: 0; padding: 0; box-sizing: border-box; }
  html, body {
    width: 856px;
    height: 1200px;
    overflow: hidden;
    background: var(--paper);
  }
  .cover {
    position: relative;
    width: 856px;
    height: 1200px;
    overflow: hidden;
    font-family: "Poppins", "Century Gothic", sans-serif;
    color: var(--ink);
  }
  .cover__texture {
    position: absolute;
    inset: 0;
    background:
      radial-gradient(ellipse at 30% 40%, var(--paper-soft) 0%, transparent 60%),
      linear-gradient(160deg, #f4f5f7 0%, var(--paper) 55%, #e6e8eb 100%);
  }
  .cover__bands {
    position: absolute;
    inset: 0;
    width: 856px;
    height: 1200px;
  }
  .brand {
    position: absolute;
    top: 200px;
    left: 0;
    width: 856px;
    text-align: center;
    color: var(--cyan);
    font-weight: 800;
    line-height: 1;
  }
  .brand__word { display: block; }
  .brand__word--main { font-size: 132px; letter-spacing: -2px; }
  .brand__word--sub { font-size: 62px; letter-spacing: 6px; margin-top: 14px; }
  .report-title {
    position: absolute;
    top: 548px;
    left: 0;
    width: 856px;
    text-align: center;
    font-size: 46px;
    font-weight: 500;
    line-height: 54px;
    letter-spacing: 0.3px;
  }
  .details {
    position: absolute;
    top: 744px;
    left: 127px;
    width: 602px;
    list-style: none;
  }
  .details__row {
    display: flex;
    align-items: flex-end;
    height: 70px;
    font-size: 21px;
    font-weight: 500;
  }
  .details__row:first-child { height: 26px; }
  .details__label { white-space: nowrap; line-height: 1; }
  .details__field {
    flex: 1;
    margin-left: 12px;
    border-bottom: 2.6px solid var(--ink);
    margin-bottom: -1px;
  }
</style>
</head>
<body>
<main class="cover">
  <div class="cover__texture" role="img" aria-label="Faint background pattern of plumbing tools: spanners, screws, nuts and pipe fittings on a light wood surface"></div>

  <svg class="cover__bands" viewBox="0 0 856 1200" aria-hidden="true">
    <defs>
      <filter id="band-shadow" x="-10%" y="-10%" width="120%" height="140%">
        <feDropShadow dx="0" dy="4" stdDeviation="3" flood-color="#000" flood-opacity="0.35"/>
      </filter>
    </defs>
    <g filter="url(#band-shadow)">
      <polygon points="0,40 215,0 375,0 0,87" fill="var(--cyan)"/>
      <polygon points="0,101 805,0 856,0 856,27 0,151" fill="var(--orange)"/>
      <polygon points="0,1196 856,1068 856,1106 212,1200 0,1200" fill="var(--orange)"/>
      <polygon points="520,1200 856,1118 856,1200" fill="var(--cyan)"/>
    </g>
  </svg>

  <h1 class="brand" aria-label="Torrent Plumbing">
    <span class="brand__word brand__word--main">TORRENT</span>
    <span class="brand__word brand__word--sub">PLUMBING</span>
  </h1>

  <h2 class="report-title">Plumbing Job Report /<br>Investigation Report</h2>

  <ul class="details">
    <li class="details__row"><span class="details__label">Client Name:</span><span class="details__field"></span></li>
    <li class="details__row"><span class="details__label">Site address:</span><span class="details__field"></span></li>
    <li class="details__row"><span class="details__label">Job reference / Work order number:</span><span class="details__field"></span></li>
    <li class="details__row"><span class="details__label">Date of attendance:</span><span class="details__field"></span></li>
    <li class="details__row"><span class="details__label">Technician / Contractor Name:</span><span class="details__field"></span></li>
  </ul>
</main>
</body>
</html>
```